Business Card Design

I am after a business card design to be made for my pet care business in Darwin, Northern Territory Australia called Waggly Whiskers. I am a certified canine trainer and offer training classes from puppy love class, basic obedience classes, intermediate classes, private lessons, mobile dog wash and grooming and pet minding. I currently have a logo that I would like used on the card that incorporates different shades of orange with the writing in black. I really want my card to stand out from the rest and look professional, easy to read with 'the edge' factor. Im thinking both sides printed on with contact details on one side and services provided on the back
Updates

Thank you all so much for your time. I am overwhelmed with designs as they are all 

really great. My business partner and myself have shortlisted a few that really caught our eye and
Will update as soon as we decide. 

Once again thank you to you all for your great designs :)

Industry/Entity Type

Training

Contact Information for Business Card

Waggly Whiskers
wagglywhiskers@mailbox-example.com
wagglywhiskers-example.com.au
0487312645
pet minding
Puppy classes
basic obedience classes
intermediate obedience classes
private lessons
mobile dog wash and grooming
certified dog trainer
CTVB certified
Police checked
fully insured
honest
reliable
find us on facebook www.socialsite-example.com/wagglywhiskers

Requirements
Must have
• My current logo either the stacked version or side by side - whatever works best and must include my services

```html
<!DOCTYPE html>
<html lang="en">
<head>
<meta charset="utf-8">
<title>Waggly Whiskers – Business Card</title>
<link href="https://fonts.googleapis.com/css2?family=Questrial&family=Dancing+Script:wght@500&display=swap" rel="stylesheet">
<style>
  :root {
    --gold: #c8961f;
    --gold-deep: #c18f1c;
    --gold-pale: #fbeed4;
    --ink: #2b2b2b;
    --ink-soft: #3a3a3a;
    --paper: #ffffff;
    --page: #ffffff;
    --photo-grass: #8a9a5a;
    --photo-path: #cfc6b8;
  }
  * { box-sizing: border-box; margin: 0; padding: 0; }
  html, body {
    width: 942px; height: 1200px; overflow: hidden;
    background: var(--page);
    font-family: "Questrial", "Century Gothic", sans-serif;
    color: var(--ink);
  }
  .card {
    position: absolute; left: 86px; width: 750px; height: 456px;
    border-radius: 34px; overflow: hidden; background: var(--paper);
    box-shadow: 0 6px 22px rgba(0,0,0,0.16);
  }
  .card--front { top: 109px; }
  .card--back { top: 653px; }

  /* Front */
  .brand__mark {
    position: absolute; left: 150px; top: 40px;
    width: 115px; height: 115px; border-radius: 50%;
    background: var(--gold); opacity: 0.85;
  }
  .brand__divider {
    position: absolute; left: 297px; top: 17px; width: 1.5px; height: 162px;
    background: var(--ink);
  }
  .brand__name {
    position: absolute; left: 333px; top: 42px;
    font-size: 50px; line-height: 62px; font-weight: 400; letter-spacing: 2px;
    color: var(--ink); text-transform: uppercase;
  }
  .tagline {
    position: absolute; left: 0; right: 0; top: 180px; text-align: center;
    font-family: "Dancing Script", cursive; font-weight: 500; font-size: 44px; color: var(--ink);
  }
  .front-rule { position: absolute; left: 0; right: 0; top: 238px; height: 9px; background: var(--gold); }
  .contact-band {
    position: absolute; left: 0; right: 0; top: 247px; bottom: 0;
    background: linear-gradient(to bottom, var(--gold-pale) 0%, #efd49c 45%, var(--gold) 100%);
  }
  .contact { position: absolute; left: 176px; top: 18px; list-style: none; }
  .contact__item { display: flex; align-items: center; height: 41px; font-size: 22px; color: var(--ink-soft); }
  .contact__icon { width: 24px; height: 24px; margin-right: 15px; flex: none; }

  /* Back */
  .services__title {
    position: absolute; left: 0; right: 0; top: 18px; text-align: center;
    font-size: 23px; font-weight: 400; color: var(--gold);
  }
  .services__list { position: absolute; top: 54px; list-style: none; }
  .services__list--left { left: 22px; }
  .services__list--right { left: 390px; top: 56px; }
  .services__item {
    position: relative; padding-left: 25px; height: 31.5px;
    font-size: 20px; line-height: 31.5px; color: var(--ink-soft); white-space: nowrap;
  }
  .services__item::before {
    content: ""; position: absolute; left: 4px; top: 12px;
    width: 7px; height: 7px; border-radius: 50%; background: var(--gold);
  }
  .back-rule { position: absolute; left: 0; right: 0; top: 200px; height: 9px; background: var(--gold-deep); }
  .photo {
    position: absolute; left: 0; right: 0; top: 209px; bottom: 0;
    background: linear-gradient(to bottom, var(--photo-grass) 0%, #a7a98a 30%, var(--photo-path) 60%, #e0d8cc 100%);
  }
</style>
</head>
<body>

<section class="card card--front">
  <div class="brand__mark"></div>
  <div class="brand__divider"></div>
  <h1 class="brand__name">Waggly<br>Whiskers</h1>
  <p class="tagline">“Happy tails, every single day”</p>
  <div class="front-rule"></div>
  <div class="contact-band">
    <ul class="contact">
      <li class="contact__item">
        <svg class="contact__icon" viewBox="0 0 24 24" fill="none" stroke="#333" stroke-width="1.6"><rect x="5" y="3" width="14" height="18" rx="2"/><line x1="11" y1="18" x2="13" y2="18"/></svg>
        0487312645
      </li>
      <li class="contact__item">
        <svg class="contact__icon" viewBox="0 0 24 24" fill="none" stroke="#333" stroke-width="1.6"><rect x="3" y="6" width="18" height="12"/><polyline points="3,6 12,13 21,6"/><line x1="3" y1="18" x2="10" y2="12"/><line x1="21" y1="18" x2="14" y2="12"/></svg>
        wagglywhiskers@mailbox-example.com
      </li>
      <li class="contact__item">
        <svg class="contact__icon" viewBox="0 0 24 24" fill="none" stroke="#333" stroke-width="1.5"><circle cx="12" cy="12" r="9"/><ellipse cx="12" cy="12" rx="4" ry="9"/><line x1="3" y1="12" x2="21" y2="12"/><line x1="12" y1="3" x2="12" y2="21"/></svg>
        www.wagglywhiskers-example.com.au
      </li>
      <li class="contact__item">
        <svg class="contact__icon" viewBox="0 0 24 24"><rect x="1" y="1" width="22" height="22" rx="3" fill="#4a6aa8"/></svg>
        www.socialsite-example.com/wagglywhiskers
      </li>
    </ul>
  </div>
</section>

<section class="card card--back">
  <h2 class="services__title">Services provided:</h2>
  <ul class="services__list services__list--left">
    <li class="services__item">Pet minding</li>
    <li class="services__item">Puppy classes</li>
    <li class="services__item">Basic obedience classes</li>
    <li class="services__item">Intermediate obedience classes</li>
  </ul>
  <ul class="services__list services__list--right">
    <li class="services__item">Private lessons</li>
    <li class="services__item">Mobile dog wash and grooming</li>
    <li class="services__item">Certified dog trainer</li>
    <li class="services__item">CTVB certified Police</li>
  </ul>
  <div class="back-rule"></div>
  <div class="photo" role="img" aria-label="Photo of a walker leading five leashed dogs along a paved park path"></div>
</section>

</body>
</html>
```